Dental Business Card

I need Dental oriented business cards.
On the front side -
- on the first line, my name:
Dr Marlow Tasker
- on the second line (just underneath):
Doctor of Dental Medicine
- on the third line, or underneath that or in a corner, I would like the address and phone number:
5192 Ch. Birchfield
Montreal QC H2P 4K8
514-629-5074
- other than that i would maybe like a logo of a tooth, but i want it to be subtle and very basic!
- I would like the card to be preferably black or dark grey-ish with the writing in white
On the other side -
- 2-3 lines with the possibility to write the next appointment the box with the lines should be white, with the rest of the card being black

```html
<!DOCTYPE html>
<html lang="en">
<head>
<meta charset="utf-8">
<title>Dr Marlow Tasker – Business Card</title>
<link href="https://fonts.googleapis.com/css2?family=Lato:wght@400;700&display=swap" rel="stylesheet">
<style>
  :root {
    --page-bg: #e4e4e4;
    --card-bg: #2a2a2a;
    --ink: #ffffff;
    --ink-soft: #f0f0f0;
  }
  * { margin: 0; padding: 0; box-sizing: border-box; }
  html, body {
    width: 1200px;
    height: 1200px;
    overflow: hidden;
    background: var(--page-bg);
    font-family: "Lato", sans-serif;
    color: var(--ink);
  }
  .canvas { position: relative; width: 1200px; height: 1200px; }
  .card {
    position: absolute;
    background: var(--card-bg);
  }
  .card--front { left: 188px; top: 90px; width: 823px; height: 475px; }
  .card--back  { left: 182px; top: 630px; width: 835px; height: 466px; }

  .practice-mark {
    position: absolute;
    left: 261px;
    top: 237px;
    transform: translate(-50%, -50%);
    display: flex;
    align-items: center;
    gap: 12px;
    white-space: nowrap;
  }
  .practice-mark__dot {
    width: 16px; height: 16px;
    border: 2px solid var(--ink);
    border-radius: 50%;
  }
  .practice-mark__name {
    font-size: 22px;
    font-weight: 400;
    color: var(--ink);
  }

  .contact {
    position: absolute;
    left: 443px;
    top: 138px;
  }
  .contact__name {
    font-size: 30px;
    font-weight: 700;
    line-height: 1.1;
  }
  .contact__title {
    font-size: 21px;
    font-weight: 400;
    line-height: 1.2;
    color: var(--ink-soft);
  }
  .contact__address {
    margin-top: 40px;
    font-size: 21px;
    line-height: 29px;
    font-style: normal;
    color: var(--ink-soft);
  }
  .contact__phone {
    margin-top: 20px;
    font-size: 21px;
    color: var(--ink-soft);
  }

  .appointment__title {
    position: absolute;
    left: 0; right: 0;
    top: 195px;
    text-align: center;
    font-size: 38px;
    font-weight: 700;
    padding-right: 20px;
  }
  .appointment__box {
    position: absolute;
    left: 178px;
    top: 272px;
    width: 482px;
    height: 110px;
    border: 2px solid var(--ink);
    padding: 24px 18px 0 14px;
  }
  .appointment__row {
    display: flex;
    align-items: baseline;
    gap: 10px;
    font-size: 22px;
    height: 42px;
  }
  .appointment__line {
    flex: 1;
    border-bottom: 1px dashed var(--ink-soft);
    transform: translateY(-2px);
  }
</style>
</head>
<body>
<main class="canvas">
  <section class="card card--front" aria-label="Card front">
    <div class="practice-mark">
      <span class="practice-mark__dot"></span>
      <span class="practice-mark__name">Tasker Dental</span>
    </div>
    <div class="contact">
      <h1 class="contact__name">Dr Marlow Tasker</h1>
      <p class="contact__title">Doctor of Dental Medicine</p>
      <address class="contact__address">5192 Ch. Birchfield<br>Montreal QC H2P 4K8</address>
      <p class="contact__phone">514-629-5074</p>
    </div>
  </section>

  <section class="card card--back" aria-label="Card back">
    <h2 class="appointment__title">Appointment</h2>
    <div class="appointment__box">
      <div class="appointment__row"><span>Time</span><span class="appointment__line"></span></div>
      <div class="appointment__row"><span>Date</span><span class="appointment__line"></span></div>
    </div>
  </section>
</main>
</body>
</html>
```